依頼詳細
・商品の特徴:現在販売している「牛ホルモン」や「豚コマ切れ」を家庭で使いたい分だけすぐに使用できる個食パックシリーズ(100g×3P)を作ります。
・価格:300円~1000円
・ターゲット層:30代~、小家族、単身者
・販売先:百貨店、デパート、通販、スーパー(ディスカウントショップ除く)

記載項目
・商品種類は10種類以上を予定しています。(バラ・コマ切れ・ぶつ切り・焼肉カットなど)
・デザインは下記の3種類からお選び下さい。
「牛ホルモン」「豚コマ切れ」「とりもも(小)」
・調理例を掲載する場合は添付写真をご利用下さい。
・袋サイズ:W255×H180
・デザインしていただく部分:W255×H180
・材質:PP
・色数:4色(白を含む)
・中身を見て購入して頂きたいので、中身が見える小窓を付けて頂きたいです。
・品名は商品の部位となります。判読性よく、大きめでお願いします。
・商品特徴を記載お願いします。(表現は自由に変更してください。何個でも使用可能です)
①肉屋の
②手軽に
③収納上手
④使い切りサイズ
⑤本格調理
⑥メインディッシュ
⑦新鮮素材
希望イメージ
シンプル 複雑
単色 カラフル
暗い 明るい
日常 高級
遊び心 厳粛
未来的 伝統的
女性的 男性的
希望する色
赤系、茶系、緑系、黄・オレンジ系、グレー系、紫系
納品ファイル
• 高解像度JPG (.jpg)
• イラストレーター形式 (.ai)
補足説明
添付のイメージ写真はあくまでもイメージとなっています。
・シリーズでの販売
・ギフトでも販売可能
・シンプルで簡潔で分かりやすいデザイン
皆さん、ご応募頂き有難うございます。
もう少しデザインを見させて頂きたいため、延長させて下さい。
何卒ご理解の程、宜しくお願い致します。
皆様、デザイン提供有難うございます。
もう少し検討時間を延長させて頂いております。
何卒ご理解の程、宜しくお願い致します。

どのデザインも素晴らしかったのですが、ニーズに沿っており弊社の女性社員投票で1位だったためです。絵も入っており、シンプル且つ可愛さがあり、目を惹くデザインでしたので選ばせて頂きました。

皆さんの素晴らしいデザインには本当に悩みました。最終的に社内投票になったのですが、どれも夢の溢れる商品開発が出来ると感じました。有難うございました。

```html
<!DOCTYPE html>
<html lang="ja">
<head>
<meta charset="utf-8">
<title>肉屋の牛ホルモン パッケージ</title>
<link rel="stylesheet" href="https://fonts.googleapis.com/css2?family=Noto+Sans+JP:wght@400;700;900&display=swap">
<style>
  :root {
    --paper: #ffffff;
    --red-deep: #7e1414;
    --red: #a81d1d;
    --black: #000000;
    --gold-light: #d2bd86;
    --gold: #b99d5f;
    --ink: #1c1008;
    --badge-red: #c8161d;
    --window: #c4c4c4;
    --mark: #333333;
  }
  html, body {
    margin: 0;
    padding: 0;
    width: 839px;
    height: 1200px;
    overflow: hidden;
    background: var(--paper);
    font-family: "Noto Sans JP", sans-serif;
  }
  .canvas {
    position: relative;
    width: 839px;
    height: 1200px;
  }
  .trim-marks {
    position: absolute;
    inset: 0;
  }
  .package {
    position: absolute;
    left: 62px;
    top: 34px;
    width: 715px;
    height: 1116px;
    background: linear-gradient(180deg, var(--red-deep) 0%, var(--red) 30%, #7a1010 52%, #2a0404 72%, var(--black) 84%, var(--black) 100%);
    overflow: hidden;
  }
  .title-panel {
    position: absolute;
    left: 16px;
    top: 282px;
    width: 684px;
    height: 322px;
    background: linear-gradient(180deg, var(--gold-light), var(--gold));
    box-shadow: 0 2px 6px rgba(0,0,0,.4);
  }
  .shop-name {
    position: absolute;
    left: 24px;
    top: 14px;
    margin: 0;
    font-weight: 900;
    font-size: 82px;
    line-height: 1;
    color: var(--ink);
    letter-spacing: 2px;
  }
  .product-name {
    position: absolute;
    left: 20px;
    top: 100px;
    margin: 0;
    font-weight: 900;
    font-size: 120px;
    line-height: 1;
    color: var(--ink);
    letter-spacing: 2px;
  }
  .description {
    position: absolute;
    right: 22px;
    top: 252px;
    margin: 0;
    font-weight: 700;
    font-size: 18px;
    line-height: 1.55;
    color: var(--ink);
    text-align: left;
  }
  .badge {
    position: absolute;
    left: 360px;
    top: 206px;
    padding: 8px 20px 12px;
    background: var(--paper);
    border: 3px solid var(--ink);
    transform: rotate(-4deg);
    font-weight: 900;
    font-size: 74px;
    line-height: 1;
    color: var(--badge-red);
    letter-spacing: 2px;
  }
  .window {
    position: absolute;
    left: 112px;
    top: 644px;
    width: 498px;
    height: 246px;
  }
  .portion {
    position: absolute;
    left: 282px;
    top: 946px;
    width: 154px;
    height: 62px;
    background: var(--paper);
    border-radius: 8px;
    display: flex;
    flex-direction: column;
    align-items: center;
    justify-content: center;
    font-weight: 700;
    font-size: 15px;
    line-height: 1.35;
    color: var(--ink);
  }
  .swatches {
    position: absolute;
    left: 504px;
    top: 1162px;
    display: flex;
    gap: 28px;
  }
  .swatch {
    width: 28px;
    height: 28px;
    box-sizing: border-box;
    border: 1px solid var(--mark);
  }
  .swatch--black { background: var(--black); }
  .swatch--gold { background: var(--gold); }
  .swatch--red { background: var(--badge-red); }
  .swatch--white { background: var(--paper); }
</style>
</head>
<body>
<div class="canvas">
  <svg class="trim-marks" width="839" height="1200" viewBox="0 0 839 1200" aria-hidden="true">
    <g stroke="var(--mark)" stroke-width="1" fill="none">
      <path d="M0 34 H50 M0 24 H40 M62 0 V22 M52 0 V14"/>
      <path d="M839 34 H789 M839 24 H799 M777 0 V22 M787 0 V14"/>
      <path d="M0 1150 H50 M0 1160 H40 M62 1200 V1162 M52 1200 V1170"/>
      <path d="M839 1150 H789 M839 1160 H799 M777 1200 V1162 M787 1200 V1170"/>
      <path d="M419 0 V22 M399 12 H439"/>
      <path d="M419 1200 V1162 M399 1188 H439"/>
      <path d="M0 592 H50 M20 572 V612"/>
      <path d="M839 592 H789 M819 572 V612"/>
    </g>
  </svg>

  <section class="package">
    <div class="title-panel">
      <h2 class="shop-name">肉屋の</h2>
      <h1 class="product-name">牛ホルモン</h1>
      <p class="description">肉屋がこだわった本格的な牛ホルモンをご家庭で<br>使いやすいように使い切りサイズの小分けパックにしました。</p>
    </div>
    <div class="badge">本格調理</div>

    <svg class="window" viewBox="0 0 498 246" role="img" aria-label="中身が見える小窓">
      <path d="M60 14 C150 -2 350 -2 440 14 C500 26 500 220 440 232 C350 248 150 248 60 232 C0 220 0 26 60 14 Z" fill="var(--window)" stroke="var(--paper)" stroke-width="8"/>
    </svg>

    <div class="portion">
      <span>使い切りサイズ</span>
      <span>（100g×3P）</span>
    </div>
  </section>

  <div class="swatches" aria-label="使用色">
    <div class="swatch swatch--black"></div>
    <div class="swatch swatch--gold"></div>
    <div class="swatch swatch--red"></div>
    <div class="swatch swatch--white"></div>
  </div>
</div>
</body>
</html>
```